Business Card Design using new attached logo

We are a family run Plumbing and Heating firm looking to improve our company image with an improved business card and new logo.We are looking to keep the company colour (Blue) involved in our design

Reason: New logo added which needs to be incorporated on designs

Industry/Entity Type

Business

Contact Information for Business Card

See attachment of all info required.

Requirements
Must have
• We have just picked a new company logo which is attached.
• Could you please provide your business card designs using this logo.
• We are looking for the logo on the back as well as the front with all the info required

```html
<!DOCTYPE html>
<html lang="en">
<head>
<meta charset="utf-8">
<title>Calder Heating Ltd – Business Cards</title>
<link href="https://fonts.googleapis.com/css2?family=Crimson+Text:wght@400;700&display=swap" rel="stylesheet">
<style>
  :root {
    --backdrop: #3b332b;
    --navy: #0c1f3f;
    --paper: #f4f4f2;
    --stripe: #8a949c;
    --ink-light: #ffffff;
    --ink-dark: #0c1f3f;
    --ink-soft: #dfe4ec;
  }
  * { margin: 0; padding: 0; box-sizing: border-box; }
  html, body {
    width: 1200px; height: 781px; overflow: hidden;
    background: var(--backdrop);
    font-family: "Crimson Text", "Times New Roman", serif;
  }
  .canvas {
    width: 1200px; height: 781px;
    display: flex; align-items: center; justify-content: center; gap: 60px;
  }
  .card {
    width: 510px; height: 330px;
    position: relative; overflow: hidden;
    box-shadow: 0 10px 28px rgba(0,0,0,.45);
  }
  /* Front */
  .card-front {
    background: var(--navy);
    display: flex; align-items: center; justify-content: center;
  }
  .brand-front {
    display: flex; align-items: center; gap: 14px;
  }
  .brand-mark {
    width: 22px; height: 22px; background: var(--ink-light);
  }
  .brand-name-front {
    color: var(--ink-light);
    font-weight: 700; font-size: 40px; letter-spacing: 2px;
    line-height: 1;
  }
  /* Back */
  .card-back { background: var(--navy); }
  .back-top {
    position: absolute; left: 0; top: 0; width: 100%; height: 150px;
    background: var(--paper);
  }
  .back-stripe {
    position: absolute; left: 0; top: 160px; width: 100%; height: 8px;
    background: var(--stripe);
  }
  .brand-back {
    position: absolute; left: 28px; top: 78px;
    display: flex; align-items: center; gap: 10px;
  }
  .brand-back .brand-mark { width: 14px; height: 14px; background: var(--ink-dark); }
  .brand-name-back {
    color: var(--ink-dark); font-weight: 700; font-size: 24px; letter-spacing: 1px; line-height: 1;
  }
  .holder {
    position: absolute; right: 30px; top: 24px; text-align: right; color: var(--ink-dark);
  }
  .holder-name { font-weight: 700; font-size: 19px; letter-spacing: 1px; }
  .holder-role { font-size: 14px; }
  .contacts {
    position: absolute; left: 28px; top: 196px; list-style: none;
    color: var(--ink-soft); font-size: 15px; line-height: 23px;
  }
  .contacts li { display: flex; align-items: center; gap: 10px; }
  .contacts svg { width: 13px; height: 13px; fill: var(--ink-soft); flex: none; }
  .address {
    position: absolute; left: 250px; top: 242px;
    display: flex; gap: 10px; color: var(--ink-soft); font-size: 15px; line-height: 21px;
  }
  .address svg { width: 13px; height: 16px; fill: var(--ink-soft); margin-top: 3px; flex: none; }
</style>
</head>
<body>
<main class="canvas">
  <section class="card card-front" aria-label="Card front">
    <div class="brand-front">
      <span class="brand-mark"></span>
      <span class="brand-name-front">CALDER HEATING LTD</span>
    </div>
  </section>

  <section class="card card-back" aria-label="Card back">
    <div class="back-top"></div>
    <div class="back-stripe"></div>
    <div class="brand-back">
      <span class="brand-mark"></span>
      <span class="brand-name-back">CALDER HEATING LTD</span>
    </div>
    <div class="holder">
      <p class="holder-name">OWEN HARTLEY</p>
      <p class="holder-role">Director</p>
    </div>
    <ul class="contacts">
      <li><svg viewBox="0 0 16 16"><path d="M3 1h3l1.5 4-2 1.2a9 9 0 0 0 4.3 4.3L11 8.5l4 1.5v3a2 2 0 0 1-2 2A12 12 0 0 1 1 3a2 2 0 0 1 2-2z"/></svg>020 7946 0132</li>
      <li><svg viewBox="0 0 16 16"><path d="M4 0h8a1 1 0 0 1 1 1v14a1 1 0 0 1-1 1H4a1 1 0 0 1-1-1V1a1 1 0 0 1 1-1zm1 2v10h6V2z"/></svg>077 00 900418</li>
      <li><svg viewBox="0 0 16 16"><path d="M4 0h7v4H4zM1 5h14v8h-3v3H4v-3H1zm5 6v3h4v-3z"/></svg>020 7946 0275</li>
      <li><svg viewBox="0 0 16 16"><path d="M0 3h16v10H0zm1.5 1.2V5l6.5 4 6.5-4v-.8L8 8z"/></svg>owenhartley@calderheating.co.uk</li>
    </ul>
    <div class="address">
      <svg viewBox="0 0 12 16"><path d="M6 0a6 6 0 0 1 6 6c0 4-6 10-6 10S0 10 0 6a6 6 0 0 1 6-6zm0 3.5A2.5 2.5 0 1 0 6 8.5a2.5 2.5 0 0 0 0-5z"/></svg>
      <p>Mill Lane, Kingsford<br>Surrey KT9 2AB</p>
    </div>
  </section>
</main>
</body>
</html>
```